Seeking funky, innovative business cards

I am looking to refresh our current business cards to something more engaging, visual and impactful. We are a management consultancy firm, see website (www.thornbury-partners.com.au). I've included our colour scheme, sample of the slides we use and our old business cards. We would like our cards to have icons. The card should display:- Name- Title- Mobile number- Address- Email address- Website - Company logo- Our purpose statement "We shape bright rooms where good teams thrive"

Contact Information for Business Card

Radek Solvieri
Consultant
0491 627 358
Level 3, 218 Wexford Street, Melbourne 3000
radek@thornbury-partners.com.au
www.thornbury-partners.com.au

Purpose statement "We shape bright rooms where good teams thrive"
LOGO available in google images

Font styles to use
Other font styles liked:
• Open Sans Light, Bebas Neue (open to other cool foints)

Colors
ffc214
5c5c5c
f5f5f5
fefefe

Requirements
Must have
• - Name
• - Title
• - Mobile number
• - Address
• - Email address
• - Website
• - Company logo
• - Our purpose statement "We shape bright rooms where good teams thrive"
Nice to have
• - Icons
• - Colour (see our colour scheme"

```html
<!DOCTYPE html>
<html lang="en">
<head>
<meta charset="utf-8">
<title>Thornbury Partners Australia – Business Cards</title>
<link rel="stylesheet" href="https://fonts.googleapis.com/css2?family=Lato:wght@300;400;700&display=swap">
<style>
  :root {
    --stage: #2b2b2b;
    --card-white: #fefefe;
    --ink-grey: #4a4d50;
    --ink-dark: #1a1a1a;
    --accent-orange: #f7a823;
    --accent-yellow: #ffc214;
    --yellow-top: #ffd60a;
    --yellow-bottom: #fdbd22;
    --rule-grey: #9a9a9a;
  }
  * { margin: 0; padding: 0; box-sizing: border-box; }
  html, body {
    width: 1200px; height: 1200px; overflow: hidden;
    background: var(--stage);
    font-family: 'Lato', sans-serif;
  }
  .card {
    position: absolute; top: 310px; height: 594px;
    box-shadow: 0 4px 10px rgba(0,0,0,0.45);
    text-align: center;
    overflow: hidden;
  }
  .card--front { left: 234px; width: 364px; background: var(--card-white); color: var(--ink-dark); }
  .card--back {
    left: 627px; width: 369px;
    background: linear-gradient(180deg, var(--yellow-top) 0%, var(--yellow-bottom) 100%);
    color: var(--ink-dark);
  }
  .brand { position: absolute; left: 0; right: 0; }
  .brand__dot {
    display: block; width: 14px; height: 14px; border-radius: 50%;
    margin: 0 auto 10px; background: var(--accent-orange);
  }
  .brand__name {
    display: block; font-weight: 300; font-size: 62px; line-height: 1; letter-spacing: 0.5px;
  }
  .brand__sub {
    display: block; font-weight: 400; font-size: 14px; letter-spacing: 2.6px;
    margin-top: 10px; text-align: right;
  }
  .card--front .brand { top: 144px; color: var(--ink-grey); }
  .card--front .brand__sub { padding-right: 40px; }
  .card--back .brand { top: 262px; color: var(--ink-dark); }
  .card--back .brand__sub { padding-right: 38px; }
  .card--back .brand__dot { background: var(--ink-dark); }
  .person { position: absolute; top: 337px; left: 0; right: 0; }
  .person__name { font-size: 22px; font-weight: 400; color: var(--accent-orange); text-transform: uppercase; line-height: 1.1; }
  .person__title { font-size: 17px; color: var(--ink-grey); margin-top: 1px; }
  .icon-row {
    position: absolute; top: 396px; left: 87px; width: 190px; height: 24px;
    display: flex; align-items: center; gap: 4px;
  }
  .icon-row__rule { flex: 1; height: 1px; background: var(--rule-grey); }
  .icon-row svg { width: 24px; height: 24px; }
  .contact { position: absolute; top: 430px; left: 0; right: 0; font-size: 17px; line-height: 22px; }
  .divider { position: absolute; top: 507px; left: 87px; width: 190px; height: 1px; background: var(--ink-grey); }
  .address { position: absolute; top: 517px; left: 0; right: 0; font-size: 17px; line-height: 22px; }
  .purpose {
    position: absolute; top: 493px; left: 0; right: 0;
    font-size: 20px; line-height: 29px; text-transform: uppercase; letter-spacing: -0.3px;
  }
</style>
</head>
<body>
  <section class="card card--front" aria-label="Business card front">
    <div class="brand">
      <span class="brand__dot"></span>
      <span class="brand__name">Thornbury</span>
      <span class="brand__sub">PARTNERS AUSTRALIA</span>
    </div>
    <div class="person">
      <p class="person__name">Radek Solvieri</p>
      <p class="person__title">Consultant</p>
    </div>
    <div class="icon-row">
      <span class="icon-row__rule"></span>
      <svg viewBox="0 0 24 24" aria-label="Phone"><circle cx="12" cy="12" r="12" fill="var(--accent-yellow)"/><path d="M6 10c0-2 2-3 6-3s6 1 6 3l-2 1-1-2H9l-1 2z M8 12h8l1 5H7z" fill="#fff"/></svg>
      <svg viewBox="0 0 24 24" aria-label="Email"><circle cx="12" cy="12" r="12" fill="var(--accent-yellow)"/><rect x="6" y="8" width="12" height="8" fill="#fff"/><path d="M6 8l6 5 6-5" fill="none" stroke="var(--accent-yellow)" stroke-width="1.2"/></svg>
      <svg viewBox="0 0 24 24" aria-label="Website"><circle cx="12" cy="12" r="12" fill="var(--accent-yellow)"/><circle cx="12" cy="12" r="6" fill="none" stroke="#fff" stroke-width="1.5"/><path d="M6 12h12M12 6c-3 3-3 9 0 12M12 6c3 3 3 9 0 12" fill="none" stroke="#fff" stroke-width="1.2"/></svg>
      <span class="icon-row__rule"></span>
    </div>
    <div class="contact">
      <p>0491 627 358</p>
      <p>radek@thornbury-partners.com.au</p>
      <p>www.thornbury-partners.com.au</p>
    </div>
    <div class="divider"></div>
    <div class="address">
      <p>Level 3, 218 Wexford</p>
      <p>Street, Melbourne 3000</p>
    </div>
  </section>

  <section class="card card--back" aria-label="Business card back">
    <div class="brand">
      <span class="brand__dot"></span>
      <span class="brand__name">Thornbury</span>
      <span class="brand__sub">PARTNERS AUSTRALIA</span>
    </div>
    <p class="purpose">We shape bright rooms<br>where good teams thrive</p>
  </section>
</body>
</html>
```